Company Flyer for Electric boating company

I am looking for a company flyer which we can hand over to boat owners in the Netherlands (Amsterdam area). Our core business is to rebuild every boat (from 4 to 10 meters) into an electrically propelled boat. We are taking out diesels and replace them with a high quality electrical motor, inboard varying from 30 till 80 pk (hp). And outboard from 1pk (hp) till 200pk. We are the best, not the cheapest, not the most expensive. We only work with the best materials. The flyer has to be sort of in line with our website and branding.

Major advantages of electric boating are:
- completely silent
- no fumes, smells or smoke
- cheap to operate
- environmentally friendly
- obliged in more and more areas
- no maintenance
- more enjoyable

The flyer should be A5 format. Since all the text has to be in Dutch I expect only the graphical design and layout for advantages, process, pricing and contact details etc.

Target Market(s)

Boat owners in the Netherlands

Font styles to use
Sans Serif

Colors
9bcb3c
add136
cadf82
0555a3
3176b5
85acd3
e0ebf3

Requirements
Must have
• Clean design, in line with website: www.volta-kade.nl
Nice to have
• icons for advantages, boating etc

2 sides
Should not have
• Steering wheel...

```html
<!DOCTYPE html>
<html lang="nl">
<head>
<meta charset="utf-8">
<title>Volta Kade – Elektrisch varen</title>
<link href="https://fonts.googleapis.com/css2?family=Oswald:wght@500;700&family=Open+Sans:wght@400;600;700&display=swap" rel="stylesheet">
<style>
  :root {
    --blue-deep: #0555a3;
    --blue-mid: #3176b5;
    --blue-soft: #85acd3;
    --blue-pale: #e0ebf3;
    --green: #9bcb3c;
    --green-bright: #add136;
    --white: #ffffff;
    --ink: #0b3f78;
  }
  * { box-sizing: border-box; margin: 0; padding: 0; }
  html, body { width: 847px; height: 1200px; overflow: hidden; background: var(--white); }
  .flyer {
    position: relative;
    width: 847px;
    height: 1200px;
    overflow: hidden;
    background: var(--white);
    font-family: "Open Sans", Arial, sans-serif;
    color: var(--ink);
  }
  .hero { position: absolute; left: 0; top: 0; width: 847px; height: 600px; }

  .brand {
    position: absolute; left: 36px; top: 22px;
    display: flex; align-items: center; gap: 14px;
    background: var(--blue-deep);
    padding: 16px 26px 16px 18px;
    border-radius: 4px;
  }
  .brand-dot { width: 46px; height: 46px; border-radius: 50%; background: var(--green); flex: none; }
  .brand-text { display: flex; flex-direction: column; font-family: "Oswald", Arial, sans-serif; font-weight: 500; color: var(--white); line-height: 1.05; }
  .brand-name { font-size: 36px; letter-spacing: 1px; text-transform: uppercase; }
  .brand-tag { font-size: 16px; letter-spacing: 1.5px; text-transform: uppercase; }

  .section-title {
    font-family: "Oswald", Arial, sans-serif;
    font-weight: 500;
    color: var(--blue-mid);
    font-size: 24px;
    letter-spacing: 1px;
    text-transform: uppercase;
  }
  .copy { font-size: 15.5px; line-height: 1.5; font-weight: 600; color: var(--ink); }

  .advantages { position: absolute; left: 40px; top: 598px; width: 350px; }
  .process { position: absolute; left: 40px; top: 800px; width: 350px; }
  .advantages .copy, .process .copy { margin-top: 12px; }

  .prices-title { position: absolute; left: 672px; top: 684px; }
  .price-card { position: absolute; top: 748px; width: 210px; font-size: 15px; line-height: 1.42; font-weight: 600; color: var(--ink); white-space: nowrap; }
  .price-card.small { left: 420px; }
  .price-card.medium { left: 628px; }
  .price-name { font-family: "Oswald", Arial, sans-serif; font-weight: 500; color: var(--blue-mid); font-size: 19px; letter-spacing: 1px; }
  .price-amount { color: var(--blue-mid); font-weight: 700; margin-bottom: 6px; }
  .price-card.small .price-name, .price-card.small .price-amount { }

  .contact { position: absolute; left: 0; bottom: 0; width: 847px; height: 170px; }
  .contact-body { position: absolute; left: 40px; top: 22px; color: var(--white); }
  .contact-title { font-family: "Oswald", Arial, sans-serif; font-weight: 500; font-size: 24px; letter-spacing: 1px; }
  .contact-lines { margin-top: 12px; font-size: 14.5px; line-height: 1.55; font-weight: 600; }
  .contact-row { display: flex; align-items: center; gap: 30px; margin-top: 4px; }
  .contact-item { display: flex; align-items: center; gap: 8px; }
  .contact-item svg { width: 18px; height: 18px; }
</style>
</head>
<body>
<div class="flyer">

  <svg class="hero" viewBox="0 0 847 600" aria-hidden="false">
    <defs>
      <linearGradient id="sky" x1="0" y1="0" x2="0" y2="1">
        <stop offset="0" stop-color="#3176b5"/>
        <stop offset="0.55" stop-color="#85acd3"/>
        <stop offset="1" stop-color="#0555a3"/>
      </linearGradient>
    </defs>
    <path d="M0 0 H847 V160 C780 150 700 170 640 140 L560 0 Z" fill="#0555a3"/>
    <path d="M0 0 H300 C270 60 250 110 200 140 C120 190 60 220 0 240 Z" fill="#0555a3"/>
    <path d="M0 240 C70 220 150 190 210 140 C260 100 300 40 330 0 H560 C600 80 640 130 720 150 C780 162 820 158 847 156 V600 H0 Z" fill="#ffffff"/>
    <path role="img" aria-label="Foto van een wit motorjacht op blauw water"
          d="M20 300 C60 250 120 220 200 190 C260 165 320 120 380 120 C440 118 500 150 560 150 C640 152 700 200 780 210 C820 215 840 240 847 260 V520 C800 540 760 520 700 540 C620 570 540 560 460 580 C380 600 300 570 220 560 C150 552 80 560 20 530 Z"
          fill="url(#sky)"/>
    <path d="M847 380 C800 430 790 470 740 520 C700 560 660 580 620 600 H847 Z" fill="#0555a3" opacity="0.85"/>
  </svg>

  <div class="brand">
    <span class="brand-dot"></span>
    <span class="brand-text">
      <span class="brand-name">Volta Kade</span>
      <span class="brand-tag">Elektrisch varen</span>
    </span>
  </div>

  <section class="advantages">
    <h2 class="section-title">Advantages</h2>
    <p class="copy">Volta Kade is persoonlijk. Wij ontmoeten onze toekomstige relaties graag en leren hun boot kennen alvorens een offerte uit te brengen. Zo komen we nooit voor verrassingen te staan.</p>
  </section>

  <section class="process">
    <h2 class="section-title">Process</h2>
    <p class="copy">Volta Kade is persoonlijk. Wij ontmoeten onze toekomstige relaties graag en leren hun boot kennen alvorens een offerte uit te brengen. Zo komen we nooit voor verrassingen te staan.</p>
  </section>

  <h2 class="section-title prices-title">Pricess</h2>

  <div class="price-card small">
    <div class="price-name">KLEIN</div>
    <div>tot 5 mtr</div>
    <div>vanaf</div>
    <div class="price-amount">€2200,-</div>
    <div>Outboard</div>
    <div>1,1kW motor (4pk)</div>
    <div>915 Wh Li-Ion</div>
    <div>GPS tracker</div>
    <div>Draagbare accu</div>
    <div>zelf te monteren</div>
    <div>perfecte vervaning voor</div>
    <div>buitenboordmotor</div>
  </div>

  <div class="price-card medium">
    <div class="price-name">KLEIN</div>
    <div>tot 5 mtr</div>
    <div>vanaf</div>
    <div class="price-amount">€2200,-</div>
    <div>Outboard</div>
    <div>1,1kW motor (4pk)</div>
    <div>915 Wh Li-Ion</div>
    <div>GPS tracker</div>
    <div>Draagbare accu</div>
    <div>zelf te monteren</div>
    <div>perfecte vervaning voor</div>
    <div>buitenboordmotor</div>
  </div>

  <footer class="contact">
    <svg width="847" height="170" viewBox="0 0 847 170" style="position:absolute;left:0;top:0">
      <path d="M0 8 C120 0 260 14 420 6 C580 -2 720 12 847 4 V170 H0 Z" fill="#0555a3"/>
    </svg>
    <div class="contact-body">
      <h2 class="contact-title">CONTACTS:</h2>
      <div class="contact-lines">
        <div>Volta Kade</div>
        <div>Havenkade 22 1021AB, Amsterdam (Noord) Nederland</div>
        <div class="contact-row">
          <span class="contact-item">
            <svg viewBox="0 0 24 24"><path d="M6.6 10.8a15.1 15.1 0 006.6 6.6l2.2-2.2c.3-.3.7-.4 1-.2 1.1.4 2.3.6 3.6.6.6 0 1 .4 1 1V20c0 .6-.4 1-1 1A17 17 0 013 4c0-.6.4-1 1-1h3.5c.6 0 1 .4 1 1 0 1.3.2 2.5.6 3.6.1.3 0 .7-.2 1z" fill="#ffffff"/></svg>
            +31 6 12 345 678
          </span>
          <span class="contact-item">
            <svg viewBox="0 0 24 24"><rect x="2" y="5" width="20" height="14" rx="2" fill="#ffffff"/><path d="M3 6l9 7 9-7" fill="none" stroke="#0555a3" stroke-width="2"/></svg>
            info@volta-kade.nl
          </span>
        </div>
      </div>
    </div>
  </footer>

</div>
</body>
</html>
```